Business Card Design Project

We are rebranding an existing automotive collision repair business. The business is called dentworks garage. I have attached logo but I'm not tied to that. I want to leave this wide open.

I want this card to say we are professional, competent, cutting edge. We are focused on customers and use a lot of the latest technology to make the customer experience different. We sign customers in on iPads. Paperwork I signed electronically and updates are sent via text, email, logging on a website or as they wish. I want this innovation and image to come through in our cards

Target Market(s)

60%. Women 40% men. Age 35-60

Industry/Entity Type

Automotive

Requirements
Must have
• The card must have name, title, phone,email, cell, web page

```html
<!DOCTYPE html>
<html lang="en">
<head>
<meta charset="utf-8">
<title>Dentworks Garage – Business Card</title>
<link rel="stylesheet" href="https://fonts.googleapis.com/css2?family=Arimo:wght@400;700&display=swap">
<style>
  :root {
    --page: #2b2b2d;
    --card: #1d1d1f;
    --card-edge: #111112;
    --green: #8cc63f;
    --white: #f2f2f2;
    --swoosh: #5a5a5e;
    --swoosh-light: #8d8d92;
  }
  * { box-sizing: border-box; margin: 0; padding: 0; }
  html, body { width: 1200px; height: 900px; overflow: hidden; }
  body {
    background: var(--page);
    font-family: "Arimo", Arial, sans-serif;
    position: relative;
  }
  .card {
    position: absolute;
    left: 330px;
    width: 540px;
    height: 310px;
    background: radial-gradient(ellipse at 40% 30%, #262628 0%, var(--card) 60%, var(--card-edge) 100%);
    box-shadow: 0 10px 30px rgba(0,0,0,.5);
    overflow: hidden;
  }
  .card--front { top: 110px; }
  .card--back { top: 470px; }
  .card__swooshes { position: absolute; inset: 0; width: 100%; height: 100%; }

  .wordmark {
    position: absolute;
    text-align: center;
    color: var(--green);
    font-weight: 700;
    line-height: 1;
    white-space: nowrap;
  }
  .card--front .wordmark { left: 0; right: 0; top: 130px; font-size: 42px; }
  .card--back .wordmark { left: 70px; width: 330px; top: 40px; font-size: 28px; }

  .address {
    position: absolute;
    left: 44px;
    top: 150px;
    font-size: 12px;
    font-style: normal;
    color: var(--white);
    line-height: 1.4;
  }
  .label { color: var(--green); }

  .contact {
    position: absolute;
    left: 300px;
    top: 146px;
    color: var(--white);
  }
  .contact__name { color: var(--green); font-weight: 700; font-size: 20px; }
  .contact__title { font-size: 11px; margin: 4px 0 10px; }
  .contact__list { list-style: none; font-size: 11.5px; line-height: 1.55; letter-spacing: .04em; }
</style>
</head>
<body>

  <section class="card card--front" aria-label="Card front">
    <svg class="card__swooshes" viewBox="0 0 540 310" aria-hidden="true">
      <path d="M120 8 Q330 -4 540 60 L540 66 Q330 10 120 8 Z" fill="var(--swoosh)"/>
      <path d="M0 300 Q260 270 540 130 L540 150 Q280 290 30 310 L0 310 Z" fill="var(--swoosh)"/>
      <path d="M60 310 Q300 270 540 160 L540 168 Q300 285 100 310 Z" fill="var(--swoosh-light)" opacity=".5"/>
    </svg>
    <p class="wordmark">Dentworks Garage</p>
  </section>

  <section class="card card--back" aria-label="Card back">
    <svg class="card__swooshes" viewBox="0 0 540 310" aria-hidden="true">
      <path d="M200 150 Q380 110 540 60 L540 72 Q380 130 200 150 Z" fill="var(--swoosh-light)" opacity=".6"/>
      <path d="M0 216 Q150 225 260 252 Q150 232 0 222 Z" fill="var(--swoosh)"/>
      <path d="M0 260 Q120 275 250 310 L220 310 Q110 282 0 266 Z" fill="var(--swoosh)" opacity=".7"/>
    </svg>
    <p class="wordmark">Dentworks Garage</p>

    <address class="address">
      <span class="label">Address:</span><br>
      2750 Harbor Lane, Riverside
    </address>

    <div class="contact">
      <p class="contact__name">Dana Whitfield</p>
      <p class="contact__title">Designer</p>
      <ul class="contact__list">
        <li><span class="label">Mob:</span> 01 2468 1357</li>
        <li><span class="label">Email:</span> dana@dentworksgarage.com</li>
        <li><span class="label">web:</span> www.dentworksgarage.com</li>
      </ul>
    </div>
  </section>

</body>
</html>
```